Independent Consultant needs jazzy website for official company launch!

I need a simple (I think), 4-6 page wordpress design for a hosted wordpress site. I have a new logo for the company (it's a puzzle piece), and business cards but no other marketing materials developed yet.

The main features of the website are Services Offered and How Clients Use Us pages and a Resources section.

Section structure:
About us
Services Offered
How Clients Use Us
Blog
Resources

Blog items
I will use keywords and comments, categories and tags.
Images will be used and should be clickable to see larger picture.

Nature of business:
-Velbor Group, Inc. is a start-up independent management consulting firm based in the Twin Cities, MN but with affiliates in other US locations. We specialize in brain-based, research-based organization development, learning, and coaching services.
- my background: organization behavior, neuroscience, training design and delivery, change management, management coaching, facilitation

Favourite colors:
- citron green
-orange
-grey
-blues - not turqoise or teal

Updates
•Instead of creating a bunch of custom css/html, i would like the final design to be based on one of these themes (these are my favorites):
Quillwhistle, Bramblet, UPelk, Lovisture, Odask, Fenwisha, Marlowbe, Glimbers, Vusko, Halberquint)

Target Market(s)
business owners, executives, mid-upper level managers in private and public sector companies

Examples of sites I kind of like:
http://www.trosnik-example.com
Updates

                                        I am posting a scanned front and back business card to give you an idea of the style I've used so far.  Thank you!

Industry/Entity Type

Management Consulting

Requirements
Must have
• resources page must be set up like a small store - i'll want to sell books, training materials from this site

also would like to build a mailing list over time so that i can send a periodic newsletter to visitors
Should not have
• difficult updates or require me to hire someone to make simple content edits - i'd like to do that on my own

don't want a lot of 'generic' people in photos on my site - would rather have a few real photos included or some visuals of symbols or objects that relate to the work provided

like bold, modern look but not too cutesy or young looking

```html
<!DOCTYPE html>
<html lang="en">
<head>
<meta charset="utf-8">
<title>Velbor Group, Inc.</title>
<link href="https://fonts.googleapis.com/css2?family=Ubuntu:wght@500;700&family=Noto+Serif:wght@400;700&display=swap" rel="stylesheet">
<style>
:root{
  --page:#3a3a3a;
  --ink:#1c1c1c;
  --white:#ffffff;
  --citron:#c9dc5a;
  --logo-green:#a5b73a;
  --orange:#e0821c;
  --panel:#ececec;
  --sidebar:#e6e6e6;
  --footer:#1d1d1d;
  --nav:#262626;
}
*{box-sizing:border-box;margin:0;padding:0}
html,body{width:705px;height:1200px;overflow:hidden;background:var(--page)}
body{font-family:"Noto Serif",Georgia,serif;color:var(--ink);font-size:8.6px;line-height:1.55}
.canvas{position:relative;width:705px;height:1200px;overflow:hidden;background:var(--page)}
.abs{position:absolute}
.top-strip{left:101px;top:0;width:571px;height:13px;background:#2c2c2c}
.sheet{left:101px;top:13px;width:571px;height:959px;background:var(--white)}

/* header */
.brand-mark{left:37px;top:22px;width:67px;height:68px;background:var(--citron);box-shadow:2px 3px 4px rgba(0,0,0,.45)}
.brand-name{left:116px;top:26px;font-family:"Ubuntu",sans-serif;font-weight:700;font-size:31px;color:var(--logo-green);letter-spacing:.3px;white-space:nowrap}
.tagline{left:117px;top:62px;font-family:"Ubuntu",sans-serif;font-weight:500;font-size:13.5px;color:#333;white-space:nowrap}
.address-box{left:492px;top:22px;width:158px;height:68px;border:1.5px solid #444;border-radius:4px;background:linear-gradient(#fff,#e4e4e4);padding:10px 0 0 26px;font-weight:700;font-size:9.2px;line-height:1.68;white-space:nowrap}
.address-box svg{position:absolute;left:8px;top:11px}

/* nav */
.nav{left:109px;top:107px;width:555px;height:29px;background:var(--nav);border-radius:3px;display:flex;font-family:"Ubuntu",sans-serif;font-weight:500;font-size:10.5px;color:#fff;letter-spacing:.4px}
.nav span{display:flex;align-items:center;justify-content:center;border-right:1px solid #555;height:100%;white-space:nowrap}
.nav .blog{background:var(--citron);color:#333;height:37px;align-items:flex-start;padding-top:7px;border-right:none;box-shadow:0 2px 3px rgba(0,0,0,.3)}

/* feature panel */
.feature-panel{left:110px;top:146px;width:553px;height:265px;background:var(--panel);border:1.5px solid #555;border-radius:6px}
.hero-image{left:114px;top:154px;width:363px;height:157px;background:linear-gradient(180deg,#eef2f6 0%,#b7c3d0 60%,#7d8b9c 100%);border:1px solid #666}
.welcome{left:114px;top:313px;width:364px;height:90px;background:var(--white);padding:2px 4px}
.welcome h2{font-size:15.5px;font-weight:700;letter-spacing:.3px;line-height:1.25}
.welcome p{font-size:7.4px;line-height:1.6}
.more{color:var(--orange);font-weight:700;font-size:8.6px;letter-spacing:.5px}
.featured{left:478px;top:168px;width:179px}
.featured-head{background:#2f2f2f;color:#fff;font-weight:700;font-size:11px;letter-spacing:.3px;padding:1px 14px;height:17px}
.featured-item{margin:6px 6px 0 20px;border-bottom:3px solid var(--orange);padding-bottom:2px}
.featured-item h3{font-size:11.4px;line-height:1.3}
.featured-item p{font-size:7.3px;line-height:1.55}

/* posts */
.post-title{left:116px;width:372px;font-size:15.5px;font-weight:700;line-height:1.25}
.post-title.single{white-space:nowrap}
.post-body{left:116px;width:362px;font-size:7.6px;line-height:12px}
.post-body p + p{margin-top:10px}
.skyline{float:right;width:181px;height:150px;margin:2px 0 2px 8px;border:1px solid #555;background:linear-gradient(180deg,#6f9ccd 0%,#a9c4de 45%,#6a7a55 62%,#5b7c3a 80%,#3a5d7a 100%)}
.post-more{left:116px}
.post-meta{left:116px;width:362px;background:var(--orange);color:#fff;font-size:6.8px;font-weight:700;padding:0 10px;height:12px;line-height:12px;white-space:nowrap}
.post-meta b{margin-right:10px}
.date{left:37px;width:64px;height:67px;background:var(--citron);border-bottom:3px solid var(--orange);text-align:center;font-weight:700;font-size:14px;line-height:1.1;padding-top:15px}

/* sidebar */
.sidebar{left:491px;top:413px;width:159px;height:543px;background:var(--sidebar)}
.search{left:497px;top:448px;width:122px;height:22px;background:#fff;border:1.5px solid #aaa;font-size:7.6px;color:#999;padding:4px 8px}
.search-btn{left:623px;top:448px;width:22px;height:22px;background:#333;border-radius:4px}
.widget-title{left:495px;width:152px;height:18px;background:var(--orange);color:#fff;font-weight:700;font-size:11px;padding:1px 7px;letter-spacing:.3px}
.widget-list{left:505px;width:140px;list-style:none;font-size:8px;line-height:15px}

/* footer */
.footer{left:101px;top:972px;width:571px;height:228px;background:var(--footer);color:#fff}
.fcol{top:10px;font-size:8.2px;line-height:14.8px}
.fcol .head{font-weight:700}
.fcol.links{font-weight:700;left:17px}
.fcol.cats{left:161px}
.footer-contact{left:323px;top:10px;font-weight:700;font-size:9.5px;line-height:1.75;white-space:nowrap}
.map{left:323px;top:47px;width:228px;height:154px;background:linear-gradient(135deg,#e9e5dc 0%,#e3dfd4 55%,#a9c4e3 70%,#c7dcb0 100%);border:1px solid #555}

/* share column */
.share{left:66px;width:30px;height:30px;border-radius:3px;background:#7a7a7a;border:1px solid #555}
</style>
</head>
<body>
<div class="canvas">
  <div class="abs top-strip"></div>
  <div class="abs sheet"></div>

  <div class="abs brand-mark" aria-hidden="true"></div>
  <div class="abs brand-name">Velbor Group, Inc.</div>
  <div class="abs tagline">Helping people and organizations thrive!</div>

  <div class="abs address-box">
    <svg width="12" height="18" viewBox="0 0 12 18" aria-hidden="true"><path d="M6 0C2.7 0 0 2.6 0 5.9 0 10 6 18 6 18s6-8 6-12.1C12 2.6 9.3 0 6 0z" fill="#e0821c"/><circle cx="6" cy="6" r="2.2" fill="#fff"/></svg>
    4870 Alderbank Road East<br>Northfield, MN 55057<br>651-555-0148
  </div>

  <nav class="abs nav">
    <span style="width:54px">HOME</span>
    <span style="width:101px">ABOUT US</span>
    <span style="width:109px">SERVICES OFFERED</span>
    <span style="width:143px">HOW CLIENTS USE US</span>
    <span class="blog" style="width:58px">BLOG</span>
    <span style="width:90px;border-right:none">RESOURCES</span>
  </nav>

  <div class="abs share" style="top:145px" role="img" aria-label="Share button"></div>
  <div class="abs share" style="top:182px" role="img" aria-label="Share button"></div>
  <div class="abs share" style="top:218px" role="img" aria-label="Share button"></div>
  <div class="abs share" style="top:254px" role="img" aria-label="Share button"></div>
  <div class="abs share" style="top:290px" role="img" aria-label="Share button"></div>
  <div class="abs share" style="top:326px" role="img" aria-label="Share button"></div>
  <div class="abs share" style="top:362px;background:#6cbf5c" role="img" aria-label="Share button"></div>

  <div class="abs feature-panel"></div>
  <div class="abs hero-image" role="img" aria-label="Business people standing on puzzle pieces"></div>
  <div class="abs welcome">
    <h2>Welcome to our site</h2>
    <p>Velbor Group, Inc. is a start-up independent management consulting firm based in the Twin Cities, MN but with affiliates in other US locations. We specialize in brain-based, research-based organization development, learning, and coaching services. My background: organization behavior, neuroscience, training design and delivery, change management,</p>
    <div class="more">...READ MORE</div>
  </div>

  <div class="abs featured">
    <div class="featured-head">FEATURED ARTICLES</div>
    <div class="featured-item">
      <h3>Welcome to our site</h3>
      <p>Velbor Group, Inc. is a start-up independent management consulting firm based</p>
      <div class="more">...READ MORE</div>
    </div>
    <div class="featured-item" style="margin-top:10px">
      <h3>Emotional Leadership</h3>
      <p>Lorem ipsum dolor sit amet, consectetur adipiscing elit. Suspendisse sed</p>
      <div class="more">...READ MORE</div>
    </div>
    <div class="featured-item" style="margin-top:10px">
      <h3>Leadership Practices</h3>
      <p>Lorem ipsum dolor sit amet, consectetur adipiscing elit. Suspendisse sed</p>
      <div class="more">...READ MORE</div>
    </div>
  </div>

  <!-- post one -->
  <div class="abs date" style="top:464px">10<br>MAR</div>
  <h2 class="abs post-title single" style="top:437px">Lorum ipsum dolor sit ad serum doe equus</h2>
  <div class="abs post-body" style="top:461px">
    <div class="skyline" role="img" aria-label="City skyline beside a river"></div>
    <p>Velbor Group, Inc. is a start-up independent management consulting firm based in the Twin Cities, MN but with affiliates in other US locations. We specialize in brain-based, research-based organization development, learning, and coaching services. My back-ground: organization behavior, neuroscience, training design and delivery, change management, management coaching, facilitation</p>
    <p>Lorem ipsum dolor sit amet, consectetur adipiscing elit. Pellentesque nisl augue, aliqua facilisis convall vitae, pharetra venenatis lacus. Morbi volutpat leo id dolor tincidunt mattis. Nam pellentesque, nisl nec imperdiet ornare, diam magna rutrum erat, nec ultricies nisi urna non magna.</p>
  </div>
  <div class="abs more post-more" style="top:662px">...READ MORE</div>
  <div class="abs post-meta" style="top:686px"><b>Comments: 10</b>Tags: Introduction, Home, Welcome, Business, Organization</div>

  <!-- post two -->
  <div class="abs date" style="top:733px">9<br>MAR</div>
  <h2 class="abs post-title" style="top:710px;width:362px">Organizational psychology for leaders seeking growth.</h2>
  <div class="abs post-body" style="top:754px">
    <p>Velbor Group, Inc. is a start-up independent management consulting firm based in the Twin Cities, MN but with affiliates in other US locations. We specialize in brain-based, research-based organization development, learning, and coaching services. My background: organization behavior, neuroscience, training design and delivery, change management, management coaching, facilitation</p>
    <p style="margin-top:14px">Lorem ipsum dolor sit amet, consectetur adipiscing elit. Pellentesque nisl augue, aliquam facilisis convall vitae, pharetra venenatis lacus. Morbi volutpat leo id dolor tincidunt mattis. Nam pellentesque, nisl nec imperdiet ornare, diam magna rutrum erat, nec ultricies nisi urna non magna. Vivamus nibh felis, dapibus sit amet ultrices luctus, consequat faucibus nunc. Nam</p>
  </div>
  <div class="abs more post-more" style="top:880px">...READ MORE</div>
  <div class="abs post-meta" style="top:901px"><b>Comments: 10</b>Tags: Introduction, Home, Welcome, Business, Organization</div>

  <aside class="abs sidebar"></aside>
  <div class="abs search">Search this site</div>
  <div class="abs search-btn"><svg width="22" height="22" viewBox="0 0 22 22" aria-hidden="true"><circle cx="9.5" cy="9.5" r="5" fill="none" stroke="#fff" stroke-width="2"/><path d="M13 13l5 5" stroke="#fff" stroke-width="2.4" stroke-linecap="round"/></svg></div>

  <div class="abs widget-title" style="top:488px">Recent Articles</div>
  <ul class="abs widget-list" style="top:510px">
    <li>Hot tea in the morning</li><li>Velmar GT</li><li>Plants I saw while in Kauai</li><li>Cruising on highway 81</li><li>Beautiful sculpture</li><li>Lemon balm leaves</li><li>Fresh poppy seeds</li>
  </ul>

  <div class="abs widget-title" style="top:645px">Archives</div>
  <ul class="abs widget-list" style="top:668px">
    <li>March 2010</li><li>February 2010</li><li>January 2010</li><li>December 2009</li><li>November 2009</li><li>October 2009</li><li>September 2009</li><li>August 2009</li><li>July 2009</li><li>June 2009</li><li>May 2009</li><li>March 2009</li>
  </ul>

  <div class="abs widget-title" style="top:874px">Tags</div>
  <ul class="abs widget-list" style="top:896px;width:142px;font-size:7.8px">
    <li>Lorem, ipsum, Dolor, organization, psychology, Structure, growth, leadership, news, Clients, relations</li>
  </ul>

  <footer class="abs footer">
    <div class="abs fcol links">About us<br>Services Offered<br>How Clients Use Us<br>Blog<br>Resources<br><br>Contact Us<br>Site Map<br><br>Privacy Policy<br>Terms of use</div>
    <div class="abs fcol cats"><span class="head">CATEGORIES</span><br>Hot Topics (222)<br>Info Brief (172)<br>Media Advisories (728)<br>News Releases (1105)<br><br><span class="head">KEY LINKS</span><br>Media contact info<br>Feeds and Publications<br>Resources and Training<br>Find an Expert</div>
    <div class="abs footer-contact">4870 Alderbank Road East Northfield, MN 55057<br>651-555-0148</div>
    <div class="abs map" role="img" aria-label="Street map showing the office location"></div>
  </footer>
</div>
</body>
</html>
```